New Business Card Design For Re-Branded Company (New Logo)

We recently switched our DBA and had a new logo designed. We now need new business cards made around our new logo. We would like to stick with the color scheme in our logo: White, Orange, and Blue. We want to see original bold designs that reflect our position in the solar energy sector but we prefer simple over complicated.

We are curious about vertical designs so if you can translate your design onto a vertical layout we would be open to look at it. We especially like a few designs we have seen on here that are vertical with a black or very dark gray background. They have our logo on one side and then the normal vertical business card on the other side.

I have included a screenshot of one of the samples we like, labeled sample.jpg and a file we were given as an example of our logo on a dark background.

At the same time we are satisfied to stay with what we have always had in a horizontal format. If it's not a lot of extra work for you, designs that are submitted in both horizontal and vertical formats will be greatly appreciated.

Please submit your original, bold, clean designs for consideration. Contact us with any questions or comments that may arise.

Thank you and Good Luck,

KP

```html
<!DOCTYPE html>
<html lang="en">
<head>
<meta charset="utf-8">
<title>Brightwell Solar – Business Card</title>
<link rel="stylesheet" href="https://fonts.googleapis.com/css2?family=Lato:wght@400;700;900&display=swap">
<style>
  :root {
    --stage: #2b2b2d;
    --card-white: #ffffff;
    --card-shade: #eeeeee;
    --brand-blue: #1f6faf;
    --brand-blue-deep: #0f5a94;
    --brand-orange: #ee7a2a;
    --ink-light: #ffffff;
    --ink-soft: #dce9f5;
    --icon-bg: #f6c9a2;
  }
  * { margin: 0; padding: 0; box-sizing: border-box; }
  html, body {
    width: 1200px; height: 997px; overflow: hidden;
    background: var(--stage);
    font-family: "Lato", Arial, sans-serif;
  }
  .stage {
    position: relative; width: 1200px; height: 997px;
    display: flex; align-items: center; justify-content: center; gap: 70px;
  }
  .card {
    border-radius: 26px; overflow: hidden; position: relative;
    box-shadow: 0 14px 40px rgba(0,0,0,.45);
  }
  /* Back side, horizontal */
  .card-back {
    width: 560px; height: 330px;
    background: linear-gradient(160deg, var(--card-white) 40%, var(--card-shade));
    display: flex; align-items: center; justify-content: center;
  }
  /* Front side, vertical */
  .card-front {
    width: 380px; height: 620px;
    background: var(--card-white);
    display: flex; flex-direction: column;
  }
  .front-header {
    height: 170px; display: flex; align-items: center; justify-content: center;
  }
  .front-body {
    flex: 1;
    background: linear-gradient(180deg, var(--brand-blue) 0%, var(--brand-blue-deep) 100%);
    padding: 52px 40px 0 44px;
    color: var(--ink-light);
    display: flex; flex-direction: column;
  }
  .brand {
    display: flex; flex-direction: column; align-items: center; gap: 10px;
  }
  .brand-dot {
    width: 44px; height: 44px; border-radius: 50%;
    background: var(--brand-orange);
  }
  .brand-name {
    font-weight: 900; font-size: 30px; letter-spacing: .5px;
    color: var(--brand-blue); text-transform: uppercase;
  }
  .card-back .brand-dot { width: 58px; height: 58px; }
  .card-back .brand-name { font-size: 40px; }
  .person-name {
    font-weight: 900; font-size: 23px; letter-spacing: 1px; text-transform: uppercase;
  }
  .person-role {
    font-size: 16px; color: var(--ink-soft); margin-top: 4px; letter-spacing: .3px;
  }
  .contact-list {
    list-style: none; margin-top: auto; margin-bottom: 70px;
    display: flex; flex-direction: column; gap: 16px;
  }
  .contact-item {
    display: flex; align-items: center; gap: 16px;
    font-size: 19px; color: var(--ink-soft);
  }
  .contact-icon {
    width: 26px; height: 26px; background: var(--icon-bg);
    display: flex; align-items: center; justify-content: center; flex: none;
  }
  .contact-icon svg { width: 16px; height: 16px; }
</style>
</head>
<body>
<main class="stage">
  <section class="card card-back" aria-label="Card back">
    <div class="brand">
      <span class="brand-dot"></span>
      <span class="brand-name">Brightwell Solar</span>
    </div>
  </section>

  <section class="card card-front" aria-label="Card front">
    <header class="front-header">
      <div class="brand">
        <span class="brand-dot"></span>
        <span class="brand-name">Brightwell Solar</span>
      </div>
    </header>
    <div class="front-body">
      <h1 class="person-name">Daniel Harrow</h1>
      <p class="person-role">Principal - Financial Planner</p>
      <ul class="contact-list">
        <li class="contact-item">
          <span class="contact-icon">
            <svg viewBox="0 0 16 16"><rect x="4" y="1" width="8" height="14" rx="1.5" fill="none" stroke="#e06a1c" stroke-width="1.8"/></svg>
          </span>0400 555 019
        </li>
        <li class="contact-item">
          <span class="contact-icon">
            <svg viewBox="0 0 16 16"><rect x="1.5" y="3.5" width="13" height="9" fill="none" stroke="#e06a1c" stroke-width="1.6"/><path d="M1.5 3.5 8 9l6.5-5.5" fill="none" stroke="#e06a1c" stroke-width="1.6"/></svg>
          </span>dan@harrowplan.com.au
        </li>
        <li class="contact-item">
          <span class="contact-icon">
            <svg viewBox="0 0 16 16"><circle cx="8" cy="8" r="6.3" fill="none" stroke="#e06a1c" stroke-width="1.5"/><ellipse cx="8" cy="8" rx="2.8" ry="6.3" fill="none" stroke="#e06a1c" stroke-width="1.3"/><path d="M1.7 8h12.6" stroke="#e06a1c" stroke-width="1.3"/></svg>
          </span>www.harrowplan.au
        </li>
      </ul>
    </div>
  </section>
</main>
</body>
</html>
```